Business Card Design for new consultancy company

Name of Company: Orbit Lanternway
Nature of Business: Digital Business Consultancy
Specialises in Digital Media Strategy, Digital Business Model Transformation, Over-The-Top (OTT) Development, Web Business Development, Digital Marketing, Web and App Product Development, Design and Innovation

Website: http://www.orbit-lanternway.example

Designs can be of any colour or any number of colours, objective is to give the impression we are a digital trend setter, creative and impactful.

Also please suggest a logo to complement the name and business card.

Target Market(s)

Media Companies, Telcos, Enterprises

Industry/Entity Type

Business

Contact Information for Business Card

Standard business card size. OK with to play with small variations like corners for impact/impression.

Font styles to use
Serif
Sans Serif

Requirements
Must have
• Clarity, Impact, Creativity
Nice to have
• Design should encapsulate professionalism, expertise, yet trend-setting and vibrant for digital consultancy
Should not have
• Messy layout, too gaudy colours or design

```html
<!DOCTYPE html>
<html lang="en">
<head>
<meta charset="utf-8">
<title>Orbit Lanternway – Business Card</title>
<link rel="stylesheet" href="https://fonts.googleapis.com/css2?family=Tinos:wght@400;700&display=swap">
<style>
  :root {
    --page-bg: #5a4632;
    --card-black: #060606;
    --brand-yellow: #e8dc0a;
    --band-yellow-light: #ece300;
    --band-yellow-dark: #c8bf00;
    --text-light: #e6e6e6;
    --text-dark: #111111;
  }
  * { box-sizing: border-box; margin: 0; padding: 0; }
  html, body {
    width: 1200px;
    height: 892px;
    overflow: hidden;
    background: var(--page-bg);
  }
  .card {
    position: absolute;
    left: 150px;
    top: 189px;
    width: 900px;
    height: 514px;
    background: var(--card-black);
    font-family: "Tinos", "Times New Roman", serif;
    color: var(--text-light);
    box-shadow: 0 10px 30px rgba(0,0,0,0.45);
    overflow: hidden;
  }
  .brand {
    position: absolute;
    left: 56px;
    top: 52px;
    width: 410px;
  }
  .brand-name {
    font-size: 54px;
    font-weight: 400;
    color: var(--brand-yellow);
    line-height: 1;
    white-space: nowrap;
  }
  .brand-tagline {
    font-size: 19px;
    margin-top: 10px;
    margin-left: 40px;
  }
  .person {
    position: absolute;
    left: 120px;
    top: 178px;
  }
  .person-name {
    font-size: 40px;
    line-height: 1;
  }
  .person-role {
    font-size: 20px;
    margin-top: 6px;
    margin-left: 28px;
  }
  .contacts {
    position: absolute;
    left: 110px;
    top: 282px;
    list-style: none;
  }
  .contacts li {
    display: flex;
    align-items: center;
    gap: 16px;
    font-size: 22px;
    line-height: 1;
    margin-bottom: 10px;
  }
  .contacts svg { width: 18px; height: 18px; flex: none; }
  .services {
    position: absolute;
    left: 500px;
    top: 84px;
    list-style: none;
  }
  .services li {
    position: relative;
    font-size: 20px;
    line-height: 1;
    padding-left: 30px;
    margin-bottom: 13px;
    white-space: nowrap;
  }
  .services li::before {
    content: "";
    position: absolute;
    left: 4px;
    top: 5px;
    width: 8px;
    height: 8px;
    background: var(--text-light);
    transform: rotate(45deg);
  }
  .address-band {
    position: absolute;
    left: 0;
    bottom: 0;
    width: 100%;
    height: 78px;
    background: linear-gradient(90deg, var(--band-yellow-dark), var(--band-yellow-light) 60%, var(--band-yellow-dark));
    display: flex;
    align-items: center;
    padding-left: 56px;
  }
  .address {
    font-size: 27px;
    font-weight: 700;
    color: var(--text-dark);
  }
</style>
</head>
<body>
  <section class="card">
    <header class="brand">
      <h1 class="brand-name">Orbit Lanternway</h1>
      <p class="brand-tagline">Digital Business Consultancy</p>
    </header>

    <div class="person">
      <p class="person-name">Employee name</p>
      <p class="person-role">Managing Director</p>
    </div>

    <ul class="contacts">
      <li>
        <svg viewBox="0 0 20 20" aria-hidden="true"><path d="M5 2 L8 2 L9 6 L7 8 Q9 12 12 13 L14 11 L18 12 L18 15 Q17 18 14 18 Q3 16 2 5 Q2 2 5 2 Z" fill="#e6e6e6"/></svg>
        <span>036-5120 7734</span>
      </li>
      <li>
        <svg viewBox="0 0 20 20" aria-hidden="true"><rect x="2" y="3" width="16" height="11" fill="none" stroke="#e6e6e6" stroke-width="2"/><rect x="8" y="14" width="4" height="3" fill="#e6e6e6"/><rect x="5" y="17" width="10" height="2" fill="#e6e6e6"/></svg>
        <span>www.yourwebsit.com</span>
      </li>
      <li>
        <svg viewBox="0 0 20 20" aria-hidden="true"><rect x="2" y="4" width="16" height="12" fill="#e6e6e6"/><path d="M2 4 L10 11 L18 4" fill="none" stroke="#060606" stroke-width="1.6"/></svg>
        <span>Info@youremail.com</span>
      </li>
    </ul>

    <ul class="services">
      <li>Specialises in Digital Media Strategy</li>
      <li>Digital Business Model Transformation</li>
      <li>Over-The-Top (OTT) Development</li>
      <li>Web Business Development</li>
      <li>Digital Marketing</li>
      <li>Web and App Product Development</li>
      <li>Design and Innovation</li>
    </ul>

    <footer class="address-band">
      <p class="address">Your Address Inc 2nd Lane Ave Millbrook,NJ&nbsp; 00000</p>
    </footer>
  </section>
</body>
</html>
```